Premium Fitness Meal Plan Design for VoltaKor (Brand Like PlumQuarry!)

VoltaKor 6 Week Autumn Forge Meal Plan Design (Branded Handout)

πŸ“„ Overview:
We are looking for a professionally designed, branded meal plan handout for our fitness facility, VoltaKor. This meal plan will be used during our upcoming 6 Week Autumn Forge Quest, where members aim to lose body fat, build lean muscle, and improve their energy through nutrition and strength training.

The design should be highly polished, visually engaging, and reflect our brand quality β€” something on par with what you would see from larger national gym chains (e.g., Plum Quarry, K62, Delmar’s Drillyard). This is not just a text document β€” we want it to feel premium, motivating, and easy to follow, ideally something members are excited to reference and share.

🧾 Format & Layout:
Size: Standard 8.5x11 inch format (single or double-sided)

Final Output: Print-ready PDF + editable source files

Orientation: Portrait

Can be designed as either:

One visually organized front-and-back sheet

Or two clean, digestible pages presented as a mini-handout

🎨 Design Style:
Clean, energetic, and transformation-focused

Use brand colors and fonts that feel bold, fresh, and motivating

Include icons, dividers, or visual cues to separate sections (not just blocks of text)

Sections should feel approachable and empowering, not clinical or restrictive

Include room for the VoltaKor logo (provided) at the top and/or footer

πŸ“˜ Content to Include:
The following content should be visually structured and formatted in clear, engaging blocks. We’ll provide this content in a PDF format

1. Header Title:
"VoltaKor 6 Week Autumn Forge Nutrition Blueprint"

2. Introduction (Small Block):
Short blurb about the challenge goals (lose body fat, gain energy, preserve lean muscle mass)

3. Elimination List (Foods to Avoid):
A visually separated section with a list of foods and drinks that should be eliminated or greatly reduced for fat loss

4. Smart Swaps Table:
A side-by-side "Craving vs Swap" table that shows easy alternatives to popular bad habits (e.g., soda β†’ sparkling water)

5. Build-Your-Own Meal Plan Sections:
Organize these into clear categories:

Proteins

Carbs

Fats

Veggies

Extras / Smart Swaps
Use icons, color codes, or visual grids to organize these food lists

6. Tips Section (Optional Bonuses):
Hydration goal

Suggested number of meals

Protein shake recommendation

Meal timing tip

10-min walk after dinner tip

πŸ“¦ Files Provided:

All written content in organized text format

βœ… Deliverables:
Final design in print-ready PDF

Editable source file (AI, PSD, or InDesign preferred)

πŸ™Œ Inspiration:
Design should feel in line with the type of professional print materials used by high-end fitness studios. Clean lines, engaging fonts, and premium layout. We're not looking for clipart or gimmicky stock photos β€” we want the design to reflect the premium, results-driven experience our gym provides.

```html
<!DOCTYPE html>
<html lang="en">
<head>
<meta charset="utf-8">
<title>VoltaKor 6 Week Autumn Forge Nutrition Blueprint – Side 1</title>
<link href="https://fonts.googleapis.com/css2?family=Arimo&family=Nunito:ital,wght@0,400;0,600;0,700;0,800;0,900;1,900&display=swap" rel="stylesheet">
<style>
  :root {
    --page-bg: #ebebeb;
    --sheet: #262626;
    --fold-line: #3a3a3a;
    --brand-yellow: #f7d000;
    --ink-dark: #262626;
    --text-light: #f1f1f1;
    --label-grey: #3a3a3a;
    --rule: #cfcfcf;
  }
  * { box-sizing: border-box; margin: 0; padding: 0; }
  html, body { width: 1200px; height: 1200px; overflow: hidden; background: var(--page-bg); }
  body { position: relative; font-family: "Nunito", sans-serif; color: var(--text-light); }

  .sheet-title {
    position: absolute; left: 0; width: 1200px; text-align: center;
    font-family: "Arimo", sans-serif; color: var(--label-grey);
    font-size: 29px; line-height: 35px; top: 153px;
  }
  .panel-label {
    position: absolute; top: 226px; width: 200px; text-align: center;
    font-family: "Arimo", sans-serif; color: var(--label-grey); font-size: 20px;
  }

  .flyer {
    position: absolute; left: 92px; top: 256px; width: 1015px; height: 785px;
    background: var(--sheet); overflow: hidden;
  }
  .panel { position: absolute; top: 0; width: 338px; height: 785px; }
  .panel--inside-left { left: 0; }
  .panel--inside-mid { left: 338px; border-left: 1px solid var(--fold-line); }
  .panel--front { left: 677px; border-left: 1px solid var(--fold-line); overflow: hidden; }
  .abs { position: absolute; }

  .intro-box {
    left: 0; top: 37px; width: 313px; height: 137px; background: var(--brand-yellow);
    color: var(--ink-dark); padding: 12px 28px 0 29px;
  }
  .intro-box h2 { font-weight: 900; font-size: 18.5px; line-height: 24px; letter-spacing: -0.2px; }
  .intro-box p { font-size: 13.2px; line-height: 15px; margin-top: 2px; }

  .food-art { border-radius: 50%; }
  .section-head { color: var(--brand-yellow); font-weight: 900; font-size: 19px; line-height: 22px; letter-spacing: -0.2px; }
  .section-sub { color: var(--text-light); font-weight: 800; font-size: 13px; line-height: 15.5px; }
  .food-list { list-style: none; }
  .food-list li {
    position: relative; padding-left: 12px; font-size: 13px; line-height: 15px; margin-bottom: 3px;
  }
  .food-list li::before {
    content: ""; position: absolute; left: 0; top: 6px; width: 4px; height: 4px;
    border-radius: 50%; background: var(--text-light);
  }
  .divider-h { height: 1px; background: var(--rule); }
  .divider-v { width: 1px; background: var(--rule); }

  .tips-head { color: var(--brand-yellow); font-weight: 900; font-size: 12.4px; line-height: 15px; letter-spacing: -0.1px; }
  .tips-list { width: 275px; }

  .brand-name {
    left: 0; width: 338px; top: 28px; text-align: center;
    color: var(--brand-yellow); font-weight: 900; font-size: 38px; line-height: 40px; letter-spacing: -0.5px;
  }
  .brand-tagline {
    left: 0; width: 338px; top: 72px; text-align: center;
    color: var(--brand-yellow); font-weight: 800; font-size: 6px; letter-spacing: 1.3px;
  }
  .title-six { left: 56px; top: 112px; color: var(--brand-yellow); font-weight: 900; font-size: 148px; line-height: 150px; letter-spacing: -4px; }
  .title-week { left: 142px; top: 168px; color: var(--brand-yellow); font-weight: 900; font-style: italic; font-size: 66px; line-height: 72px; letter-spacing: -2px; }
  .title-theme { left: 59px; top: 232px; color: var(--brand-yellow); font-weight: 900; font-style: italic; font-size: 31px; line-height: 38px; letter-spacing: -1.2px; }
  .title-main { left: 57px; top: 279px; color: #ffffff; font-weight: 900; font-size: 42px; line-height: 41px; letter-spacing: -0.5px; }
  .goal-badge {
    left: 59px; top: 392px; width: 56px; height: 27px; background: var(--brand-yellow);
    color: var(--ink-dark); font-weight: 900; font-size: 19px; line-height: 27px; text-align: center; z-index: 2;
  }
  .goal-copy { left: 59px; top: 431px; width: 130px; font-size: 13px; line-height: 15px; z-index: 2; }
  .meal-photo {
    left: 14px; top: 446px; width: 324px; height: 339px; z-index: 0;
    background:
      radial-gradient(circle at 88% 40%, #e9e4dc 0 30%, transparent 31%),
      radial-gradient(circle at 25% 80%, #8fa326 0 17%, transparent 18%),
      linear-gradient(160deg, transparent 40%, #2f3a1d 100%);
  }
</style>
</head>
<body>

  <div class="sheet-title">8.5X11 inch - 2 Fold Flyer<br>Side 1</div>
  <div class="panel-label" style="left:161px">5</div>
  <div class="panel-label" style="left:499px">6</div>
  <div class="panel-label" style="left:838px">Front</div>

  <main class="flyer">

    <section class="panel panel--inside-left">
      <div class="abs intro-box">
        <h2>BUILD-YOUR-OWN<br>MEAL PLAN GUIDE</h2>
        <p>Use these fit-friendly food lists to mix &amp; match meals. Your job: choose 1 protein, 1 carb (if desired), and 1 fat or veggie at each meal. Keep it simple, keep it consistent.</p>
      </div>

      <div class="abs food-art" role="img" aria-label="Illustration of protein foods: meat, cheese, fish, eggs and milk"
           style="left:34px;top:200px;width:80px;height:66px;border-radius:40px 40px 30px 30px;background:radial-gradient(circle at 50% 35%,#fbe6a0,#e9b97a 70%,#c98f5c);"></div>
      <div class="abs section-head" style="left:126px;top:211px">PROTEINS</div>
      <div class="abs section-sub" style="left:126px;top:231px">(choose 1 per<br>meal/snack)</div>
      <ul class="abs food-list" style="left:36px;top:274px;width:116px">
        <li>Chicken breast or thighs (air fried or grilled)</li>
        <li>Lean ground beef (90/10 or better)</li>
        <li>Ground turkey or turkey breast</li>
        <li>Center-cut pork chops</li>
        <li>Eggs / Egg whites</li>
        <li>Tuna (canned in water)</li>
      </ul>
      <ul class="abs food-list" style="left:179px;top:274px;width:116px">
        <li>Salmon or white fish</li>
        <li>Shrimp</li>
        <li>Greek yogurt (plain, low sugar)</li>
        <li>Cottage cheese (low-fat)</li>
        <li>Protein powder (whey or plant-based)</li>
        <li>Deli turkey (low-sodium)</li>
      </ul>

      <div class="abs divider-h" style="left:34px;top:488px;width:270px"></div>

      <div class="abs food-art" role="img" aria-label="Illustration of carb foods: flour, bread, rice and pasta"
           style="left:32px;top:506px;width:82px;height:66px;border-radius:40px 40px 30px 30px;background:radial-gradient(circle at 50% 40%,#eef4fb,#8fbde0 60%,#5c97c9);"></div>
      <div class="abs section-head" style="left:127px;top:505px">CARBS</div>
      <div class="abs section-sub" style="left:127px;top:526px">(choose 1–2 servings<br>per day, timed post-<br>workout or morning)</div>
      <ul class="abs food-list" style="left:36px;top:587px;width:116px">
        <li>Jasmine or basmati rice (white or brown)</li>
        <li>Sweet potatoes or yams</li>
        <li>Rolled oats or steel cut oats</li>
        <li>Quinoa</li>
        <li>Zephran bread</li>
      </ul>
      <ul class="abs food-list" style="left:178px;top:587px;width:114px">
        <li>Rice cakes</li>
        <li>Berries (blueberries, raspberries, strawberries)</li>
        <li>Apples / Bananas</li>
        <li>Chickpeas or black beans (in moderation)</li>
      </ul>
    </section>

    <section class="panel panel--inside-mid">
      <div class="abs food-art" role="img" aria-label="Illustration of fat foods: olive oil, nuts, cheese and sweets"
           style="left:36px;top:48px;width:90px;height:66px;border-radius:45px 45px 24px 24px;background:radial-gradient(circle at 50% 40%,#f6c9cf,#e79aa8 60%,#a2486a);"></div>
      <div class="abs section-head" style="left:36px;top:126px">FATS</div>
      <div class="abs section-sub" style="left:36px;top:149px">(add small<br>amounts to meals,<br>2–4 servings/day)</div>
      <ul class="abs food-list" style="left:35px;top:205px;width:122px">
        <li>Avocado or guacamole</li>
        <li>Olive oil or avocado oil (cooking or drizzle)</li>
        <li>Nut butters (almond, peanut – natural only)</li>
        <li>Whole eggs</li>
        <li>Nuts (almonds, walnuts – portion controlled)</li>
        <li>Chia seeds or flax seeds</li>
      </ul>

      <div class="abs divider-v" style="left:177px;top:50px;height:380px"></div>

      <div class="abs food-art" role="img" aria-label="Illustration of vegetables: greens, pumpkin, corn and tomatoes"
           style="left:204px;top:48px;width:90px;height:66px;border-radius:45px 45px 24px 24px;background:radial-gradient(circle at 50% 40%,#d9efe6,#84c6ad 55%,#3f8a4c);"></div>
      <div class="abs section-head" style="left:194px;top:129px">VEGGIES</div>
      <div class="abs section-sub" style="left:204px;top:149px">(unlimited –<br>fill your plate!)</div>
      <ul class="abs food-list" style="left:196px;top:205px;width:116px">
        <li>Spinach, kale, arugula</li>
        <li>Zucchini, asparagus, bell peppers</li>
        <li>Broccoli, cauliflower, green beans</li>
        <li>Cucumber, tomatoes, shredded carrots</li>
        <li>Mixed greens or salad kits (watch the dressing)</li>
      </ul>

      <div class="abs tips-head" style="left:34px;top:464px">BONUS TIPS FOR MAXIMUM RESULTS</div>
      <ul class="abs food-list tips-list" style="left:35px;top:482px">
        <li>Drink 80–120 oz. water daily — hydration is key for fat loss and muscle performance</li>
        <li>Eat 3–4 meals per day — spaced every 3–4 hours</li>
        <li>Include protein in every meal to stabilize blood sugar and support muscle</li>
        <li>Post-workout meal = protein + carb, no added fats</li>
        <li>Up to, two protein shakes per day is allowed, especially post-workout or on busy days</li>
        <li>Limit “treat” meals to 1 per week (keep it controlled)</li>
      </ul>

      <div class="abs tips-head" style="left:34px;top:700px">OPTIONAL HABITS TO STACK</div>
      <ul class="abs food-list tips-list" style="left:35px;top:718px">
        <li>Weigh in once per week (same day/time)</li>
        <li>Prep 2–3 proteins and</li>
      </ul>
    </section>

    <section class="panel panel--front">
      <div class="abs brand-name">VoltaKor</div>
      <div class="abs brand-tagline">PERSONAL GROUP TRAINING</div>

      <h1>
        <span class="abs title-six">6</span>
        <span class="abs title-week">Week</span>
        <span class="abs title-theme">Autumn Forge</span>
        <span class="abs title-main">NUTRITION<br>BLUEPRINT</span>
      </h1>

      <div class="abs meal-photo" role="img" aria-label="Photo of a plate with grilled chicken, broccoli, tomatoes and avocado slices, a fork and a halved avocado"></div>

      <div class="abs goal-badge">Goal</div>
      <p class="abs goal-copy">Drop body fat, maintain lean muscle, and boost energy without giving up real food or living in the kitchen.</p>
    </section>

  </main>
</body>
</html>
```